brightwave Marine

we need a business card with our new design from pixel forum that we just purchased. it needs to have our phone numbers, email address, web address and facebook address

Target Market(s)

Wealthy boat owners

Industry/Entity Type

Marine

Contact Information for Business Card

Business logo
Phone numbers Greg - 0408315962
Mandy - 0419486027
ABN - 61273059184
Email - brightwavemarineboatcleaning@examplemail.com
Web address - www.brightwavemarine.com.au
Facebook- Brightwave Marine

Number of Pages Required

1 page

Font styles to use
Serif
Sans Serif
Script

Colors
3276b5
33a6d7
474747
333333

Requirements
Must have
• Business logo and all contact details

```html
<!DOCTYPE html>
<html lang="en">
<head>
<meta charset="utf-8">
<title>Brightwave Marine — Business Card</title>
<link rel="stylesheet" href="https://fonts.googleapis.com/css2?family=Arimo:wght@400;700&display=swap">
<style>
  :root {
    --backdrop: #2b2b2b;
    --card: #f4f4f2;
    --brand-blue: #33a6d7;
    --deep-blue: #3276b5;
    --ink: #333333;
    --ink-soft: #474747;
  }
  * { box-sizing: border-box; margin: 0; padding: 0; }
  html, body {
    width: 1200px; height: 1200px; overflow: hidden;
    background: var(--backdrop);
    font-family: "Arimo", Arial, sans-serif;
  }
  .stage {
    width: 1200px; height: 1200px;
    display: flex; align-items: center; justify-content: center;
  }
  .business-card {
    position: relative;
    width: 1000px; height: 580px;
    background: var(--card);
    border-radius: 44px;
  }
  .brand {
    position: absolute;
    left: 470px; top: 130px;
    display: flex; align-items: center; gap: 14px;
  }
  .brand-dot {
    width: 20px; height: 20px; border-radius: 50%;
    background: var(--brand-blue);
  }
  .brand-name {
    font-size: 42px; font-weight: 700;
    color: var(--brand-blue);
    white-space: nowrap;
  }
  .contact-list {
    position: absolute;
    left: 80px; top: 296px;
    list-style: none;
  }
  .contact-item {
    display: flex; align-items: center; gap: 14px;
    height: 40px;
    font-size: 21px; color: var(--ink);
    white-space: nowrap;
  }
  .contact-icon { width: 22px; height: 22px; flex: none; }
  .contact-icon svg { width: 22px; height: 22px; display: block; }
  .social-mark {
    width: 20px; height: 20px; border-radius: 50%;
    background: var(--brand-blue); margin: 1px;
  }
  .contact-label { color: var(--brand-blue); font-weight: 700; }
  .person {
    position: absolute;
    left: 620px; top: 300px;
  }
  .person-name {
    font-size: 30px; font-weight: 700;
    color: var(--brand-blue);
  }
  .person-role {
    margin-top: 6px;
    font-size: 26px; color: var(--ink);
  }
</style>
</head>
<body>
<main class="stage">
  <section class="business-card">
    <div class="brand">
      <span class="brand-dot"></span>
      <span class="brand-name">Brightwave Marine</span>
    </div>

    <ul class="contact-list">
      <li class="contact-item">
        <span class="contact-icon"><svg viewBox="0 0 24 24"><path fill="#33a6d7" d="M12 2a7 7 0 0 0-7 7c0 5 7 13 7 13s7-8 7-13a7 7 0 0 0-7-7zm0 9.5A2.5 2.5 0 1 1 12 6.5a2.5 2.5 0 0 1 0 5z"/></svg></span>
        456 Forth Eve.
      </li>
      <li class="contact-item">
        <span class="contact-icon"><svg viewBox="0 0 24 24"><path fill="#33a6d7" d="M6.6 10.8a15 15 0 0 0 6.6 6.6l2.2-2.2a1 1 0 0 1 1-.25 11.4 11.4 0 0 0 3.6.6 1 1 0 0 1 1 1V20a1 1 0 0 1-1 1A17 17 0 0 1 3 4a1 1 0 0 1 1-1h3.5a1 1 0 0 1 1 1c0 1.25.2 2.45.6 3.6a1 1 0 0 1-.25 1z"/></svg></span>
        Greg 0408315962 &nbsp;·&nbsp; Mandy 0419486027
      </li>
      <li class="contact-item">
        <span class="contact-icon"><svg viewBox="0 0 24 24"><rect x="2" y="5" width="20" height="14" rx="1.5" fill="#33a6d7"/><path d="M3 6l9 7 9-7" fill="none" stroke="#f4f4f2" stroke-width="1.6"/></svg></span>
        brightwavemarineboatcleaning@examplemail.com
      </li>
      <li class="contact-item">
        <span class="contact-icon"><span class="social-mark"></span></span>
        facebook/Brightwave Marine
      </li>
      <li class="contact-item">
        <span class="contact-icon"><svg viewBox="0 0 24 24"><circle cx="12" cy="12" r="9" fill="none" stroke="#33a6d7" stroke-width="2"/><ellipse cx="12" cy="12" rx="4" ry="9" fill="none" stroke="#33a6d7" stroke-width="1.6"/><path d="M3 12h18" stroke="#33a6d7" stroke-width="1.6"/></svg></span>
        www.brightwavemarine.com.au
      </li>
      <li class="contact-item">
        <span class="contact-icon"></span>
        <span><span class="contact-label">ABN</span> 61273059184</span>
      </li>
    </ul>

    <div class="person">
      <p class="person-name">Mandy Green</p>
      <p class="person-role">Founder &amp; Director</p>
    </div>
  </section>
</main>
</body>
</html>
```